New website for Pollard Law Firm at www.keepwinning-example.com

We are a professional law firm located in the Nashville, Tennessee USA area. We focus on personal injury law. We are looking for a slick new website that is user friendly for updating with new blogs, videos, etc. The primary colors should be red, black, and white. It should load extremely fast and have a good mobile component. The pages for the design will include a home page, about us, news, contact us, and practice page. The practice page will be copied for all the practice areas including motor vehicle accidents, slip and fall accidents, dog bites, etc. We have included an image which we would like to include in the new site which shows the color scheme The image is called banner-Car Wreck. The new website should NOT have gavels, court houses, law books, scales or the typical images for a law firm.

Target Market(s)

People in Tennessee involved in accidents

Industry/Entity Type

Legal services, law firm

Coding

Coded - Design and coding required

Number of Pages Required

5+ page

Font styles to use
Serif

Colors
EB3D1F
EC4F4E
F09395
F8D3D4
FCEDEE

Requirements
Should not have
• Gavels, columns, scales, law related images

```html
<!DOCTYPE html>
<html lang="en">
<head>
<meta charset="utf-8">
<title>Latest News – Pollard Law Firm</title>
<link href="https://fonts.googleapis.com/css2?family=Playfair+Display:wght@600;700&family=Poppins:wght@400;500;600;700&display=swap" rel="stylesheet">
<style>
:root{
  --red:#d22b2b;
  --red-dark:#b91f22;
  --ink:#1a1a1a;
  --text:#555;
  --muted:#8a8a8a;
  --hero:#f2f2f2;
  --line:#e6e6e6;
  --footer:#1b1b1b;
  --footer-bar:#151515;
  --white:#fff;
}
*{box-sizing:border-box;margin:0;padding:0}
html,body{width:685px;height:1200px;overflow:hidden}
body{position:relative;background:var(--white);font-family:"Poppins",sans-serif;color:var(--ink)}
a{color:inherit;text-decoration:none}
.abs{position:absolute}

/* header */
.site-header{position:absolute;left:0;top:0;width:685px;height:49px}
.brand{position:absolute;left:50px;top:14px;font-family:"Playfair Display",serif;font-weight:700;font-size:14px;color:var(--red);letter-spacing:.3px}
.brand-rule{position:absolute;left:50px;top:33px;width:112px;height:1px;background:#666}
.main-nav{position:absolute;left:283px;top:20px;display:flex;gap:12px;font-size:7.5px;font-weight:500;letter-spacing:.2px}
.main-nav .active{color:var(--red)}
.main-nav .active::before{content:"";position:absolute;top:-20px;width:22px;height:1.5px;background:var(--red)}
.call{position:absolute;left:530px;top:13px;display:flex;align-items:center;gap:6px}
.call-icon{width:23px;height:23px;background:var(--red);display:flex;align-items:center;justify-content:center}
.call small{display:block;font-size:5.5px;font-weight:600;color:var(--muted)}
.call strong{display:block;font-size:10px;font-weight:600}

/* hero */
.hero{position:absolute;left:0;top:49px;width:685px;height:114px;background:var(--hero)}
.hero h1{position:absolute;left:0;width:685px;top:38px;text-align:center;font-family:"Playfair Display",serif;font-size:30px;font-weight:700}
.hero-art{position:absolute;right:0;top:14px;width:155px;height:100px;background:radial-gradient(ellipse at 60% 60%,#c9262c 0%,#8c1a1f 45%,rgba(60,70,90,.35) 70%,rgba(242,242,242,0) 85%)}

/* posts */
.post{position:absolute;left:51px;width:434px;height:137px;background:var(--white);box-shadow:0 6px 16px rgba(0,0,0,.06);display:flex}
.post-media{width:140px;height:137px;flex:none}
.post-body{padding:24px 20px 0 20px}
.post-meta{font-size:6px;color:var(--muted);font-weight:500}
.post-meta span{margin:0 3px}
.post-title{font-size:9.5px;font-weight:600;margin-top:8px}
.post-excerpt{font-size:7.6px;line-height:11.6px;color:var(--text);margin-top:6px}
.learn{display:inline-block;margin-top:9px;font-size:6.8px;font-weight:600;color:var(--red);border-bottom:1px solid var(--red)}

/* pagination */
.pager{position:absolute;left:52px;top:828px;display:flex;align-items:center}
.pager .arrow{width:22px;height:22px;border-radius:50%;background:var(--ink);display:flex;align-items:center;justify-content:center}
.pager .num{width:20px;height:20px;border-radius:50%;display:flex;align-items:center;justify-content:center;font-size:9px;margin-left:6px}
.pager .current{background:var(--red);color:var(--white)}

/* sidebar */
.sidebar{position:absolute;left:515px;top:215px;width:120px}
.sidebar h3{font-size:8.5px;font-weight:600}
.search{margin-top:6px;height:25px;background:var(--hero);display:flex;align-items:center;justify-content:space-between;padding:0 10px;font-size:6.5px;color:#666}
.search i{border-left:1px solid #ccc;height:12px;margin-left:auto;margin-right:6px}
.cats{list-style:none;margin-top:9px}
.cats li{font-size:7.6px;color:var(--text);margin-bottom:6.5px}
.more{display:inline-block;font-size:7.5px;font-weight:600;color:var(--red);border-bottom:1px solid var(--red)}
.divider{height:1px;background:#ccc;margin:16px 0 24px}
.recent{display:flex;gap:5px;margin-top:10px;margin-bottom:15px}
.recent .thumb{width:47px;height:40px;flex:none}
.recent time{display:block;font-size:5.8px;color:var(--muted);margin-top:4px}
.recent p{font-size:6.6px;line-height:8.5px;margin-top:4px}

/* footer */
.site-footer{position:absolute;left:0;top:917px;width:685px;height:283px;background:var(--footer);color:var(--white)}
.f-brand{position:absolute;left:52px;top:110px;font-family:"Playfair Display",serif;font-weight:700;font-size:19px;color:var(--red)}
.f-rule{position:absolute;left:52px;top:137px;width:138px;height:1px;background:#ddd}
.site-footer h4{position:absolute;font-size:11px;font-weight:600}
.quick{position:absolute;left:234px;top:98px;list-style:none;font-size:7px}
.quick li{margin-bottom:9px}
.contact{position:absolute;left:332px;top:98px;font-size:7px;line-height:12.5px}
.contact .row{position:relative;padding-left13px;padding-left:13px;margin-bottom:8px}
.contact svg{position:absolute;left:0;top:2px}
.nl-text{position:absolute;left:486px;top:96px;width:130px;font-size:7px;line-height:10px}
.nl-form{position:absolute;left:487px;top:125px;width:147px;height:25px;background:var(--white);display:flex;align-items:center}
.nl-form span{flex:1;font-size:7px;color:#333;padding-left:18px}
.nl-form b{width:23px;height:25px;background:var(--red);display:flex;align-items:center;justify-content:center}
.social{position:absolute;left:487px;top:160px;display:flex;gap:4px}
.social i{width:20px;height:20px;border-radius:50%;background:#2d2d2d;display:block}
.footer-bar{position:absolute;left:4px;top:248px;width:681px;height:35px;background:var(--footer-bar);border-top:1px solid #2a2a2a;text-align:center;font-size:6.8px;font-weight:600;line-height:35px}
.to-top{position:absolute;left:653px;top:238px;width:20px;height:20px;border-radius:50%;background:var(--white);display:flex;align-items:center;justify-content:center}
</style>
</head>
<body>

<header class="site-header">
  <div class="brand">Pollard Law Firm</div>
  <div class="brand-rule"></div>
  <nav class="main-nav">
    <a href="#">HOME</a><a href="#">ABOUT US</a><a href="#">PRACTICES</a><a href="#" class="active">NEWS</a><a href="#">CONTACT US</a>
  </nav>
  <div class="call">
    <div class="call-icon">
      <svg width="10" height="10" viewBox="0 0 24 24"><path fill="#fff" d="M6.6 10.8a15 15 0 0 0 6.6 6.6l2.2-2.2c.3-.3.7-.4 1-.2 1.1.4 2.3.6 3.6.6.6 0 1 .4 1 1V20c0 .6-.4 1-1 1A17 17 0 0 1 3 4c0-.6.4-1 1-1h3.5c.6 0 1 .4 1 1 0 1.3.2 2.5.6 3.6.1.3 0 .7-.2 1z"/></svg>
    </div>
    <div><small>CALL NOW</small><strong>(615) 555-0142</strong></div>
  </div>
</header>

<section class="hero">
  <h1>Latest News</h1>
  <div class="hero-art" role="img" aria-label="Red car crashing with shattering glass"></div>
</section>

<article class="post" style="top:216px">
  <div class="post-media" role="img" aria-label="Warning triangle on a wet road behind a stopped car" style="background:linear-gradient(180deg,#3f6a98,#5c7fa6 55%,#45536a)"></div>
  <div class="post-body">
    <div class="post-meta">By Daniel<span>•</span>January 2021</div>
    <h2 class="post-title">Trucking Company Offers 6 Figure Settlement</h2>
    <p class="post-excerpt">On a Thursday afternoon, our client was traveling to work when suddenly a semi-truck ran through a stop sign and crashed into the side of our client’s truck causing him...</p>
    <a class="learn" href="#">LEARN MORE</a>
  </div>
</article>

<article class="post" style="top:364px">
  <div class="post-media" role="img" aria-label="Injured man lying on a floor holding his shoulder" style="background:linear-gradient(160deg,#e6e8ec,#b9bcc3 50%,#8f8a84)"></div>
  <div class="post-body">
    <div class="post-meta">By Daniel<span>•</span>January 2021</div>
    <h2 class="post-title">DCS Chooses to Dismiss Case</h2>
    <p class="post-excerpt">In a case in Nashville, Davidson County, the Tennessee Department of Children’s Services was contacted with claims of abuse to a child by her father.&nbsp; The odd thing was that...</p>
    <a class="learn" href="#">LEARN MORE</a>
  </div>
</article>

<article class="post" style="top:512px">
  <div class="post-media" role="img" aria-label="Dog biting a person’s forearm" style="background:linear-gradient(150deg,#b7c0cc,#7a6a5a 50%,#c9a58a)"></div>
  <div class="post-body">
    <div class="post-meta">By Daniel<span>•</span>January 2021</div>
    <h2 class="post-title">Pollard Obtains Jury Verdict of 61 x Medical Bills</h2>
    <p class="post-excerpt">In 2016, a client was traveling down a road and stopped in traffic when she was hit by another driver in the rear end.&nbsp; Although she thought she was okay, she immediately began...</p>
    <a class="learn" href="#">LEARN MORE</a>
  </div>
</article>

<article class="post" style="top:660px">
  <div class="post-media" role="img" aria-label="Red car crash with flying glass on black" style="background:radial-gradient(ellipse at 55% 55%,#c8242b,#6e1117 55%,#0d0d0d 85%)"></div>
  <div class="post-body">
    <div class="post-meta">By Daniel<span>•</span>January 2021</div>
    <h2 class="post-title">Insurance Company Pays for Facial Fractures</h2>
    <p class="post-excerpt">On a dark night in Murfreesboro, Tennessee, a young woman was riding in the car with her friends when the driver decided to try to spin the car to make doughnuts.&nbsp; Unfortunately...</p>
    <a class="learn" href="#">LEARN MORE</a>
  </div>
</article>

<nav class="pager">
  <a class="arrow" href="#"><svg width="8" height="8" viewBox="0 0 10 10"><path d="M6.5 1.5 3 5l3.5 3.5" stroke="#fff" stroke-width="1.6" fill="none"/></svg></a>
  <a class="num" href="#" style="margin-left:14px">1</a>
  <a class="num" href="#">2</a>
  <a class="num current" href="#">3</a>
  <a class="num" href="#">4</a>
  <a class="num" href="#">9</a>
  <a class="arrow" href="#" style="margin-left:22px"><svg width="8" height="8" viewBox="0 0 10 10"><path d="M3.5 1.5 7 5 3.5 8.5" stroke="#fff" stroke-width="1.6" fill="none"/></svg></a>
</nav>

<aside class="sidebar">
  <h3>Search</h3>
  <div class="search">Search our store<i></i>
    <svg width="8" height="8" viewBox="0 0 12 12"><circle cx="5" cy="5" r="3.8" stroke="#333" stroke-width="1.2" fill="none"/><path d="m8 8 3 3" stroke="#333" stroke-width="1.2"/></svg>
  </div>
  <h3 style="margin-top:20px">Categories</h3>
  <ul class="cats">
    <li>Motor vehicle accidents</li><li>Dog bites</li><li>Slip and fall ccidents</li><li>Personal Injury</li>
  </ul>
  <a class="more" href="#">More</a>
  <div class="divider"></div>
  <h3>Recent Articles</h3>
  <div class="recent">
    <div class="thumb" role="img" aria-label="Worker falling from a ladder" style="background:linear-gradient(150deg,#6d8fb8,#c9a24a 60%,#3b3b3b)"></div>
    <div><time>25-02-2021</time><p>Insurance Company Pays for Facial...</p></div>
  </div>
  <div class="recent">
    <div class="thumb" role="img" aria-label="Overturned red truck" style="background:linear-gradient(150deg,#9aa0a8,#b52a2e 55%,#4a4a4a)"></div>
    <div><time>25-02-2021</time><p>Pollard Obtains Jury Verdict of...</p></div>
  </div>
  <div class="recent">
    <div class="thumb" role="img" aria-label="Woman lying on the ground after a fall" style="background:linear-gradient(150deg,#c7b9a6,#8fb0d4 60%,#d9cfc2)"></div>
    <div><time>25-02-2021</time><p>DCS Chooses to Dismiss Case</p></div>
  </div>
  <a class="more" href="#">More</a>
</aside>

<footer class="site-footer">
  <div class="f-brand">Pollard Law Firm</div>
  <div class="f-rule"></div>

  <h4 style="left:234px;top:66px">Quick Links</h4>
  <ul class="quick">
    <li>Home</li><li>About us</li><li>Practices&nbsp; Areas</li><li>News</li><li>Contact us</li>
  </ul>

  <h4 style="left:332px;top:66px">Contact info</h4>
  <div class="contact">
    <div class="row"><svg width="8" height="6" viewBox="0 0 8 6"><rect width="8" height="6" fill="#d22b2b"/><path d="M0 0l4 3 4-3" stroke="#1b1b1b" stroke-width=".8" fill="none"/></svg>Email:<br>office@pollardlaw-example.com</div>
    <div class="row"><svg width="8" height="8" viewBox="0 0 24 24"><path fill="#d22b2b" d="M6.6 10.8a15 15 0 0 0 6.6 6.6l2.2-2.2c.3-.3.7-.4 1-.2 1.1.4 2.3.6 3.6.6.6 0 1 .4 1 1V20c0 .6-.4 1-1 1A17 17 0 0 1 3 4c0-.6.4-1 1-1h3.5c.6 0 1 .4 1 1 0 1.3.2 2.5.6 3.6.1.3 0 .7-.2 1z"/></svg>Phone:<br>(615) 555-0142</div>
    <div class="row"><svg width="7" height="9" viewBox="0 0 10 14"><path fill="#d22b2b" d="M5 0a5 5 0 0 0-5 5c0 4 5 9 5 9s5-5 5-9a5 5 0 0 0-5-5zm0 7a2 2 0 1 1 0-4 2 2 0 0 1 0 4z"/></svg>Location:<br>1480 Cedar Ridge Drive<br>Suite 210, Maple Square<br>Franklin, TN 37064</div>
  </div>

  <h4 style="left:486px;top:67px">Newsletter</h4>
  <p class="nl-text">Subscribe to our email address to get the latest news.</p>
  <div class="nl-form"><span>Enter Your Email...</span>
    <b><svg width="10" height="10" viewBox="0 0 12 12"><path d="M1 6 11 1 8 11 6 7z" fill="#fff"/></svg></b>
  </div>
  <div class="social"><i></i><i></i><i></i><i></i></div>

  <div class="footer-bar">© 2021 POLLARD LAW FIRM, PLLC.&nbsp; ALL RIGHTS RESERVED.</div>
  <a class="to-top" href="#"><svg width="8" height="8" viewBox="0 0 10 10"><path d="M5 9V1M2 4l3-3 3 3" stroke="#1b1b1b" fill="none"/></svg></a>
</footer>

</body>
</html>
```